EILT: Landing Page - EXPRESS VERSAND
Zielgruppe
Es soll in kurzer Zeit (max 48 Stunden) eine kleine Ladingpage entstehen. Expressversand / Import von China nach Deutschland . Aufgrund der stark steigenden Luftfrachtraten aus China heraus hat sich unsere Firma Fracht-Kapazitäten gesichert. Diese sollen nun angeboten werden. Über eine Ladingpage sollen Anfragen generiert werden. Diese Anfragen werden dann mit einem Angebot von uns beantwortet. Expressversand / Import von China nach Deutschland
Aufgabenstellung
Die Seite soll beinhalten:
- 1-2 Bilder (z. B. Luftfracht, Logistik, Flugzeug, Cargo, etc)
- kurzer erklärender Text: z.B. 'jetzt Angebot anfordern und günstig aus China per Express versenden.' Inkl. Abholung, Verzollung und Zustellung. Kurze Laufzeit von nur 3-5 Tagen. ab 45€ / Paket
- Anfrage Formular, bestehend aus: , Abholadresse in China/Post Code, ZielAdresse Deutschland, Sendungsinformationen (wie viele Kartons, wie schwer ist ein Karton und welche Abmessungen L/B/H ), wann ist die Sendung in China abholbereit, optional: Sendungsinhalt (Ware, Zolltarifnummer/HS Code) , Firma, Name, email adresse
- optional ein Header/Laufband etc mit: Bis zum 19. Nov 21 versenden - Ware bis MegaSonntag erhalten!
- 24h Servicehotline, Tel: 0987/314265
- 2-3 Kundenreferenzen: Bilder von Personen mit Text : „Schneller Versand - nur 4 Tage Laufzeit“ , „1A Service, ohne Probleme“ , „gute Preise - nur zu empfehlen.“
Unser Firmenlogo kann - muss aber nicht auftauchen.
In der farblichen Gestaltung haben Sie freie Hand und freuen uns auf Ihre Vorschläge.
Aufgrund der Dringlichkeit sollte diese Landingpage innerhalb 48 Stunden 'live ' gehen.
WICHTIG: Die Page sollte von Ihnen auch veröffentlich werden. Aktuell nutzen wir den Kelvo Homepagebaukasten. Die Page kann aber auch durch andere Anbieter veröffentlicht werden , zb Pagerune

```html
<!DOCTYPE html>
<html lang="de">
<head>
<meta charset="utf-8">
<title>Korva Services – Express Versand aus China</title>
<link href="https://fonts.googleapis.com/css2?family=Poppins:wght@500;600;700&family=Roboto:wght@400;500;700&display=swap" rel="stylesheet">
<style>
:root{
  --navy:#0f1a45;
  --navy-deep:#0b1440;
  --panel:#0d173f;
  --blue:#29a8e0;
  --white:#ffffff;
  --muted:#aeb6cf;
  --ink:#0f1a45;
  --field-border:#e3e6ee;
  --field-text:#8b91a3;
}
*{margin:0;padding:0;box-sizing:border-box}
html,body{width:1200px;height:2218px;overflow:hidden;background:var(--white)}
body{position:relative;font-family:'Roboto',sans-serif;color:var(--ink)}
.site-header{position:absolute;left:0;top:0;width:1200px;height:75px;background:var(--white)}
.brand{position:absolute;left:160px;top:22px;display:flex;align-items:center;gap:8px;font-family:'Poppins',sans-serif;font-weight:600;font-size:22px;color:#3b4360}
.brand-dot{width:30px;height:30px;border-radius:50%;background:var(--blue)}
.header-cta{position:absolute;left:924px;top:22px;width:115px;height:30px;background:var(--blue);color:var(--white);font-size:11px;font-weight:700;display:flex;align-items:center;justify-content:center;gap:4px}
.hero{position:absolute;left:0;top:75px;width:1200px;height:427px;overflow:hidden;
  background:
    radial-gradient(ellipse 260px 180px at 1090px 180px,rgba(200,40,40,.55),transparent 70%),
    radial-gradient(ellipse 420px 200px at 380px 330px,rgba(214,196,170,.75),transparent 70%),
    linear-gradient(180deg,#7d8390 0%,#9a8b7c 45%,#c09266 62%,#5e5654 100%)}
.hero-shade{position:absolute;inset:0;background:linear-gradient(90deg,rgba(20,20,40,.45),rgba(20,20,40,.12))}
.hero h1{position:absolute;left:158px;top:78px;font-family:'Poppins',sans-serif;font-weight:700;font-size:40px;line-height:53px;color:var(--white)}
.hero p{position:absolute;left:161px;top:194px;font-weight:700;font-size:17px;line-height:29px;color:var(--white)}
.features{position:absolute;left:0;top:502px;width:1200px;height:606px;background:var(--navy)}
.eyebrow{position:absolute;width:1200px;text-align:center;top:80px;font-size:10.5px;font-weight:700;color:var(--blue)}
.features h2{position:absolute;width:1200px;text-align:center;top:98px;font-family:'Poppins',sans-serif;font-weight:600;font-size:26px;color:var(--white)}
.features .lead{position:absolute;width:1200px;text-align:center;top:142px;font-size:12.5px;line-height:19px;color:var(--muted)}
.feature-card{position:absolute;top:212px;width:203px;height:169px;border:1px solid #26305c;padding:22px 10px 0 22px}
.feature-card svg{width:38px;height:38px;display:block}
.feature-card h3{margin-top:16px;font-family:'Poppins',sans-serif;font-weight:500;font-size:14px;line-height:20px;color:var(--white)}
.feature-card p{margin-top:13px;font-size:10.5px;line-height:18px;letter-spacing:-.1px;color:var(--muted)}
.features .tagline{position:absolute;width:1200px;text-align:center;top:408px;font-size:11px;font-weight:500;color:#c6cbe0}
.tagline a{color:var(--blue);text-decoration:none;border-bottom:1px solid var(--blue);padding-bottom:2px}
.quote-band{position:absolute;left:131px;top:988px;width:945px;height:120px;background:var(--panel)}
.quote-band span{position:absolute;left:74px;top:23px;font-size:12px;font-weight:700;color:var(--blue)}
.quote-form{position:absolute;left:161px;top:1049px;width:638px;height:510px;background:var(--white);box-shadow:0 10px 30px rgba(15,26,69,.08)}
.form-label{position:absolute;left:37px;font-size:10.5px;font-weight:700;color:var(--ink)}
.field{position:absolute;height:38px;border:1px solid var(--field-border);font-size:9.5px;color:var(--field-text);padding-left:14px;display:flex;align-items:center;white-space:nowrap}
.submit{position:absolute;left:38px;top:442px;width:562px;height:38px;background:var(--navy-deep);color:var(--white);font-size:10.5px;font-weight:700;display:flex;align-items:center;justify-content:center}
.promo{position:absolute;left:799px;top:1049px;width:240px;height:510px;background:var(--blue);padding:198px 20px 0 39px;font-family:'Poppins',sans-serif;font-weight:600;font-size:19px;line-height:25.5px;color:var(--white)}
.customers h2{position:absolute;width:1200px;text-align:center;top:1612px;font-family:'Poppins',sans-serif;font-weight:600;font-size:26px;color:var(--ink)}
.testimonial{position:absolute;top:1679px;width:278px}
.testimonial .photo{width:278px;height:277px}
.testimonial p{margin-top:17px;text-align:center;font-family:'Poppins',sans-serif;font-weight:500;font-size:13.5px;color:var(--ink);white-space:nowrap}
.hotline{position:absolute;left:0;top:2068px;width:1200px;height:150px;background:var(--navy-deep);text-align:center}
.hotline h3{margin-top:40px;font-family:'Poppins',sans-serif;font-weight:600;font-size:19px;color:var(--white)}
.hotline .tel{margin-top:4px;font-family:'Poppins',sans-serif;font-weight:700;font-size:33px;color:var(--blue)}
</style>
</head>
<body>
<header class="site-header">
  <div class="brand"><span class="brand-dot"></span>KORVA SERVICES</div>
  <div class="header-cta">Request A Quote
    <svg width="10" height="10" viewBox="0 0 10 10"><path d="M1 5h7M5 2l3 3-3 3" stroke="#fff" stroke-width="1.4" fill="none"/></svg>
  </div>
</header>

<section class="hero" role="img" aria-label="Luftfracht-Paletten vor einem Frachtflugzeug auf dem Vorfeld bei Sonnenuntergang">
  <div class="hero-shade"></div>
  <h1>jetzt Angebot anfordern und günstig<br>aus China per Express versenden</h1>
  <p>Inkl. Abholung, Verzollung und Zustellung.<br>Kurze Laufzeit von nur 3-5 Tagen. ab 45€ / Paket</p>
</section>

<section class="features">
  <div class="eyebrow">Our Features</div>
  <h2>Why Choose Us!</h2>
  <p class="lead">We continue to pursue that same vision in today's complex, uncertain world,<br>working every day to earn our customers' trust!</p>

  <div class="feature-card" style="left:161px">
    <svg viewBox="0 0 38 38" fill="none" stroke="#29a8e0" stroke-width="1.4"><rect x="2" y="10" width="28" height="24" rx="2"/><rect x="8" y="3" width="14" height="9"/><rect x="24" y="18" width="12" height="8" rx="2"/><path d="M14 19v10M11 22c0-2 6-2 6 0s-6 2-6 4 6 2 6 0"/></svg>
    <h3>Transparent Pricing</h3>
    <p>International supply chains<br>involves challenging regulations.</p>
  </div>
  <div class="feature-card" style="left:387px">
    <svg viewBox="0 0 38 38" fill="none" stroke="#29a8e0" stroke-width="1.4"><circle cx="15" cy="15" r="12"/><circle cx="15" cy="15" r="8"/><path d="M11 13l4-2 4 2v5l-4 2-4-2zM11 13l4 2 4-2M15 15v5M24 24l11 11"/></svg>
    <h3>Real-Time Tracking</h3>
    <p>Ensure customers' supply chains<br>are fully compliant by practices.</p>
  </div>
  <div class="feature-card" style="left:611px">
    <svg viewBox="0 0 38 38" fill="none" stroke="#29a8e0" stroke-width="1.4"><path d="M2 2h5v30h30"/><rect x="11" y="14" width="13" height="17"/><rect x="20" y="4" width="13" height="14"/><circle cx="10" cy="35" r="2"/><path d="M25 4v5h3V4"/></svg>
    <h3>Warehouse Storage</h3>
    <p>Depending on your product, we<br>provide warehouse activities.</p>
  </div>
  <div class="feature-card" style="left:836px">
    <svg viewBox="0 0 38 38" fill="none" stroke="#29a8e0" stroke-width="1.4"><path d="M19 2l15 5v11c0 9-7 15-15 18C11 33 4 27 4 18V7z"/><path d="M19 7l10 3v8c0 6-5 11-10 13-5-2-10-7-10-13v-8z"/><path d="M14 15l5-3 5 3v6l-5 3-5-3zM14 15l5 3 5-3M19 18v6"/></svg>
    <h3>Security For Cargo</h3>
    <p>High security requirements and<br>are certified to local standards.</p>
  </div>

  <p class="tagline">Working every day to earn our customers' trust. <a>Get Started!</a></p>
</section>

<div class="quote-band"><span>Request A Quote</span></div>

<form class="quote-form">
  <div class="form-label" style="top:34px">Shipping Address</div>
  <div class="field" style="left:38px;top:59px;width:172px">Abholadresse in China</div>
  <div class="field" style="left:232px;top:59px;width:173px">Post Code</div>
  <div class="field" style="left:428px;top:59px;width:172px">ZielAdresse Deutschland</div>

  <div class="form-label" style="top:125px">Sendungsinformationen</div>
  <div class="field" style="left:38px;top:150px;width:172px">wie viele Kartons</div>
  <div class="field" style="left:232px;top:150px;width:79px">Weight</div>
  <div class="field" style="left:326px;top:150px;width:79px">Height</div>
  <div class="field" style="left:428px;top:150px;width:78px">Width</div>
  <div class="field" style="left:522px;top:150px;width:78px">Length</div>
  <div class="field" style="left:38px;top:204px;width:172px">wann ist die Sendung in China abholbereit</div>

  <div class="form-label" style="top:263px">optional: Sendungsinhalt</div>
  <div class="field" style="left:38px;top:288px;width:172px">Ware</div>
  <div class="field" style="left:232px;top:288px;width:173px">Zolltarifnummer</div>
  <div class="field" style="left:428px;top:288px;width:172px">HS Code</div>

  <div class="form-label" style="top:348px">Personal Data</div>
  <div class="field" style="left:38px;top:373px;width:172px">Firma</div>
  <div class="field" style="left:232px;top:373px;width:173px">Name</div>
  <div class="field" style="left:428px;top:373px;width:172px">email adresse</div>

  <div class="submit">Request A Quote</div>
</form>
<aside class="promo">Bis zum 19. Nov 21 versenden - Ware bis MegaSonntag erhalten!</aside>

<section class="customers">
  <h2>Our Customers</h2>
  <figure class="testimonial" style="left:161px">
    <div class="photo" role="img" aria-label="Porträtfoto eines Kunden im weißen Hemd" style="background:linear-gradient(180deg,#8f8d89 0%,#6a6460 45%,#d8d6d1 100%)"></div>
    <p>Schneller Versand - nur 4 Tage Laufzeit</p>
  </figure>
  <figure class="testimonial" style="left:461px">
    <div class="photo" role="img" aria-label="Porträtfoto einer lachenden Kundin in heller Bluse" style="background:linear-gradient(180deg,#c8b596 0%,#b38462 45%,#9eb1c2 100%)"></div>
    <p>1A Service, ohne Probleme</p>
  </figure>
  <figure class="testimonial" style="left:761px">
    <div class="photo" role="img" aria-label="Porträtfoto eines Kunden im karierten roten Hemd" style="background:linear-gradient(180deg,#b9a595 0%,#86624f 45%,#b84a4c 100%)"></div>
    <p>gute Preise - nur zu empfehlen.</p>
  </figure>
</section>

<footer class="hotline">
  <h3>24h Servicehotline</h3>
  <div class="tel">Tel: 0987/314265</div>
</footer>
</body>
</html>
```